Bref créative
brochure and folder for a4 brochures
Brush Wave
Protecting your assets
Need a brochure template to use for Strata painting and residential painting
"STRATA BROCHURE COPY"
Brush Wave, the easy choice for strata paint works
Why strata managers love Brush Wave
Work with a company that focuses on your needs – a company that can get your strata painting works done with no hassle. We’ve been in business for over 20 years; we’re your one-stop shop for painting and remedial maintenance, and we get it right the first time.
At Brush Wave, we understand you need:
• Quality painting, project managed by us so you don’t have to take endless phone calls
• Great-value price: We take time to make sure of this
• Great ideas for colour schemes (saving the owners up to $700)
• Remedial repairs overseen by a qualified master builder
Why choose Brush Wave?
The Brush Wave difference means we turn up when we’re supposed to and finish on schedule. All our tradespeople are friendly, professional – and we promise that your site will be cleaner when we’ve finished than when we started.
Once you’ve accepted our quote, we can start within 24 hours and we manage the job from start to finish. You’ll be a hero with owners and you have peace of mind knowing the job’s under control.
Life’s easier with Brush Wave
Take the headache out of your strata painting works. Call Brush Wave on 1300 482 915.
What clients say about us
“Derek and his team have skilfully and professionally painted our property comprising 17 apartments and townhouses. The progress of the work has been clean and efficient and the result is excellent.”
Owen Falkirk, Moorings, Henley
“Communication is the key to successfully managing a project and Derek and his team exceeded expectations with updates concerning all aspects of the work.“ Neil Barker, Randwick
Add value to your new home before you move in, with Brush Wave
"RESIDENTIAL BROCHURE"
Start your new life with a clean freshly painted house
We’ve been in business for over 20 years and we know that when you move into your new home, it’s best to do all the basics first – quickly, with no fuss.
At Brush Wave, we understand you want:
• Quick, clean work: We can start within 24 hours and be in and out before you know it
• Good value: We also make remedial repairs so you get a perfect finish
• Great ideas for colour schemes (saving you up to $700)
• Friendly professional tradies you’ll be happy to have around your home
We turn up when we’re supposed to and finish on time. We’ll quote as soon as you pick up the keys and can advise on colours that will create just the right atmosphere. What’s more, your new home will be cleaner than when we started.
We guarantee
• Great-value price: We’ll help you make sure of this
• Impressive service: Fast, clean, quality job, and responsive to your needs
For feel-good factor, there’s nothing like a fresh splash of colour
If you’d like to start fresh, call Brush Wave on 1300 482 915.
"When dealing with Brush Wave we were given expert and professional advice in choosing colours for our beach house... The end result was great." Fiona Darrowby
Real Estate
corporate FOR STRATA
professional FOR RESIDENTIAL
need one brochure for residential painting and one for strata painting and a folder that we can use for both brochures
please use logo only do not use NSW or website under logo
please see attachment
please only use brushwave not background, lines or website under logo
another log for your use

```html
<!DOCTYPE html>
<html lang="en">
<head>
<meta charset="utf-8">
<title>Brush Wave – Residential Brochure Covers</title>
<link href="https://fonts.googleapis.com/css2?family=Cinzel:wght@400;600;700&family=Cormorant+Garamond:ital,wght@1,600&display=swap" rel="stylesheet">
<style>
  :root{
    --bg:#e6e6e7;
    --paper:#ffffff;
    --navy:#2b2f86;
    --purple:#5a2d8c;
    --red:#d9262b;
    --orange:#f0741f;
    --yellow:#f6c21b;
    --sky-haze:#c9d3dc;
    --sky-top:#9fb0c0;
    --tower-light:#8a96a2;
    --tower-mid:#5d6a77;
    --tower-warm:#7a6f66;
    --city-dark:#2e353d;
    --shadow:rgba(0,0,0,.2);
  }
  *{box-sizing:border-box;margin:0;padding:0}
  html,body{width:1200px;height:901px;overflow:hidden;background:var(--bg)}
  body{font-family:"Cinzel",Georgia,serif;position:relative}
  .spread{position:absolute;left:80px;top:100px;width:1040px;height:700px;display:flex;gap:60px}
  .page{position:relative;width:490px;height:700px;background:var(--paper);box-shadow:0 8px 22px var(--shadow);overflow:hidden}
  .stripes{position:absolute;left:0;width:100%;display:block;z-index:2}
  .city-photo{position:absolute;left:0;width:100%;
    background:
      radial-gradient(ellipse 55% 35% at 30% 18%,rgba(255,255,255,.45),rgba(255,255,255,0) 70%),
      radial-gradient(ellipse 40% 30% at 75% 55%,rgba(220,226,232,.35),rgba(220,226,232,0) 70%),
      radial-gradient(ellipse 50% 35% at 20% 80%,rgba(122,111,102,.55),rgba(122,111,102,0) 70%),
      linear-gradient(175deg,var(--sky-haze) 0%,var(--sky-top) 14%,var(--tower-light) 32%,var(--tower-mid) 58%,var(--tower-warm) 74%,var(--city-dark) 100%)}
  .brand{display:flex;align-items:center;gap:8px;color:var(--navy);font-weight:700;letter-spacing:.03em;white-space:nowrap}
  .brand-dot{width:13px;height:13px;border-radius:50%;background:var(--red);flex:none}

  /* back cover */
  .back .stripes.top{top:14px}
  .back .city-photo{top:36px;height:534px}
  .back .stripes.bottom{top:548px}
  .call-bar{position:absolute;left:0;top:590px;width:100%;height:36px;background:var(--navy);z-index:3;
    color:#fff;font-family:"Cormorant Garamond",Georgia,serif;font-style:italic;font-weight:600;font-size:21px;
    display:flex;align-items:center;padding-left:26px;white-space:nowrap}
  .call-bar .phone{color:var(--orange);margin-left:7px}
  .back .brand{position:absolute;right:30px;top:646px;font-size:21px}

  /* front cover */
  .front .brand{position:absolute;left:52px;top:30px;font-size:28px}
  .front .stripes.top{top:64px}
  .front .city-photo{top:86px;height:470px;clip-path:polygon(0 9%,45% 5.5%,100% 0,100% 100%,0 100%)}
  .front .stripes.bottom{top:528px}
  .headline{position:absolute;right:28px;top:608px;text-align:right;font-size:19px;line-height:1.4;font-weight:600;text-transform:uppercase;white-space:nowrap}
  .headline .line-1{color:var(--navy);display:block}
  .headline .line-2{color:var(--red);display:block}
</style>
</head>
<body>
<main class="spread">

  <section class="page back" aria-label="Back cover">
    <svg class="stripes top" height="30" viewBox="0 0 490 30" preserveAspectRatio="none">
      <path d="M0 4 L490 16" stroke="var(--yellow)" stroke-width="4"/>
      <path d="M0 9 L490 21" stroke="var(--red)" stroke-width="3.5"/>
      <path d="M0 14 L490 26" stroke="var(--navy)" stroke-width="3.5"/>
    </svg>
    <div class="city-photo" role="img" aria-label="Aerial photograph of a dense city skyline with high-rise towers"></div>
    <svg class="stripes bottom" height="44" viewBox="0 0 490 44" preserveAspectRatio="none">
      <path d="M0 2 L490 26" stroke="var(--yellow)" stroke-width="4"/>
      <path d="M0 7 L490 31" stroke="var(--red)" stroke-width="3.5"/>
      <path d="M0 12 L490 36" stroke="var(--purple)" stroke-width="4"/>
      <path d="M0 20 L490 44" stroke="#fff" stroke-width="10"/>
    </svg>
    <div class="call-bar">Call Brush Wave on<span class="phone">1300 482 915.</span></div>
    <div class="brand"><span class="brand-dot"></span>Brush Wave</div>
  </section>

  <section class="page front" aria-label="Front cover">
    <div class="brand"><span class="brand-dot"></span>Brush Wave</div>
    <svg class="stripes top" height="50" viewBox="0 0 490 50" preserveAspectRatio="none">
      <path d="M0 40 Q250 28 490 4" fill="none" stroke="var(--purple)" stroke-width="4"/>
      <path d="M0 45 Q250 33 490 9" fill="none" stroke="var(--red)" stroke-width="3.5"/>
      <path d="M0 50 Q250 38 490 14" fill="none" stroke="var(--yellow)" stroke-width="4"/>
    </svg>
    <div class="city-photo" role="img" aria-label="Aerial photograph of city rooftops and skyscrapers"></div>
    <svg class="stripes bottom" height="60" viewBox="0 0 490 60" preserveAspectRatio="none">
      <path d="M0 60 L490 60 L490 16 Q250 26 0 52 Z" fill="#fff"/>
      <path d="M0 42 Q250 18 490 4" fill="none" stroke="var(--yellow)" stroke-width="4"/>
      <path d="M0 47 Q250 23 490 9" fill="none" stroke="var(--red)" stroke-width="3.5"/>
      <path d="M0 52 Q250 28 490 14" fill="none" stroke="var(--navy)" stroke-width="4"/>
    </svg>
    <h1 class="headline">
      <span class="line-1">Start your new life with a</span>
      <span class="line-2">clean freshly painted house</span>
    </h1>
  </section>

</main>
</body>
</html>
```